Business Card Design

Consultant ot credit unions that operate a property and casualty insurance agency

Industry/Entity Type

Insurance

Contact Information for Business Card

Dorian Velker
Credit Union Insurance Agency Consultant
dorianvelker@mailvoro.com
562 318-4092
914 Tamsin Court
Long Beach, CA 90813

```html
<!DOCTYPE html>
<html lang="en">
<head>
<meta charset="utf-8">
<title>Dorian Velker – Business Card</title>
<link rel="stylesheet" href="https://fonts.googleapis.com/css2?family=Cinzel:wght@400;500;600&display=swap">
<style>
  :root {
    --page-bg: #e6e4e1;
    --card-white: #f7f7f7;
    --card-grey: #dcdcdc;
    --ink: #141414;
    --band-black: #0e0e0e;
    --band-edge: #3a3a3a;
    --band-text: #f2f2f2;
    --detail-text: #4a4a4a;
    --divider: #9a9a9a;
  }
  * { margin: 0; padding: 0; box-sizing: border-box; }
  html, body {
    width: 1200px;
    height: 1023px;
    overflow: hidden;
    background: var(--page-bg);
  }
  .stage {
    width: 1200px;
    height: 1023px;
    display: flex;
    align-items: center;
    justify-content: center;
  }
  .business-card {
    position: relative;
    width: 840px;
    height: 480px;
    overflow: hidden;
    background: linear-gradient(160deg, var(--card-white) 0%, #ffffff 40%, var(--card-grey) 100%);
    box-shadow: 0 14px 40px rgba(0,0,0,0.25);
    font-family: "Cinzel", serif;
  }
  .card-name {
    position: absolute;
    top: 78px;
    left: 0;
    width: 100%;
    text-align: center;
    font-size: 66px;
    font-weight: 500;
    letter-spacing: 3px;
    color: var(--ink);
  }
  .title-band {
    position: absolute;
    top: 196px;
    left: 0;
    width: 100%;
    height: 54px;
    background: linear-gradient(180deg, var(--band-edge) 0%, var(--band-black) 22%, var(--band-black) 78%, var(--band-edge) 100%);
    display: flex;
    align-items: center;
    justify-content: center;
  }
  .title-band .job-title {
    color: var(--band-text);
    font-size: 25px;
    font-weight: 500;
    letter-spacing: 1.5px;
  }
  .contact-row {
    position: absolute;
    top: 282px;
    left: 0;
    width: 100%;
    display: flex;
    justify-content: center;
    align-items: stretch;
    color: var(--detail-text);
    font-size: 17px;
    letter-spacing: 1px;
  }
  .contact-address {
    text-align: right;
    padding-right: 22px;
    line-height: 34px;
  }
  .contact-divider {
    width: 1px;
    background: var(--divider);
  }
  .contact-lines {
    padding-left: 22px;
    line-height: 34px;
  }
  .contact-line {
    display: flex;
    align-items: center;
    gap: 9px;
  }
  .contact-line svg { flex: none; }
  .bottom-swoosh {
    position: absolute;
    left: 0;
    bottom: 0;
    width: 840px;
    height: 130px;
  }
</style>
</head>
<body>
<main class="stage">
  <section class="business-card">
    <h1 class="card-name">Dorian Velker</h1>

    <div class="title-band">
      <p class="job-title">Credit Union Insurance Agency Consultant</p>
    </div>

    <div class="contact-row">
      <address class="contact-address" style="font-style: normal;">
        914 Tamsin Court<br>
        Long Beach, CA 90813
      </address>
      <span class="contact-divider"></span>
      <div class="contact-lines">
        <p class="contact-line">
          <svg width="14" height="10" viewBox="0 0 14 10" aria-hidden="true">
            <rect x="0.5" y="0.5" width="13" height="9" fill="#4a4a4a"/>
            <path d="M0.5 0.5 L7 5.5 L13.5 0.5" fill="none" stroke="#f7f7f7" stroke-width="1.2"/>
          </svg>
          dorianvelker@mailvoro.com
        </p>
        <p class="contact-line">
          <svg width="14" height="14" viewBox="0 0 24 24" aria-hidden="true">
            <path fill="#4a4a4a" d="M6.6 10.8a15.1 15.1 0 0 0 6.6 6.6l2.2-2.2a1 1 0 0 1 1-.25 11.4 11.4 0 0 0 3.6.57 1 1 0 0 1 1 1V20a1 1 0 0 1-1 1A17 17 0 0 1 3 4a1 1 0 0 1 1-1h3.5a1 1 0 0 1 1 1c0 1.25.2 2.45.57 3.57a1 1 0 0 1-.25 1z"/>
          </svg>
          562 318-4092
        </p>
      </div>
    </div>

    <svg class="bottom-swoosh" viewBox="0 0 840 130" preserveAspectRatio="none" aria-hidden="true">
      <defs>
        <linearGradient id="swooshFill" x1="0" y1="0" x2="0" y2="1">
          <stop offset="0" stop-color="#2c2c2c"/>
          <stop offset="0.5" stop-color="#0c0c0c"/>
          <stop offset="1" stop-color="#000000"/>
        </linearGradient>
      </defs>
      <path d="M0 40 C 240 110, 560 120, 840 70 L840 130 L0 130 Z" fill="url(#swooshFill)"/>
      <path d="M0 72 C 260 126, 580 128, 840 96" fill="none" stroke="#8c8c8c" stroke-width="3" opacity="0.75"/>
      <path d="M0 40 C 240 110, 560 120, 840 70" fill="none" stroke="#555" stroke-width="1.5"/>
    </svg>
  </section>
</main>
</body>
</html>
```